buseisness card

design a card that similar to my web site
BRIXENTAPLORLLC .COM

Contact Information for Business Card

NAME PHONE # WEBSITE EMAIL AND DISCTIPTION OF WHAT WE DO

Colors
0054AA
0677BA
7BADD7
CADEEF
E8F1F8

Requirements
Must have
• lOGO AND DETAILS
Nice to have
• I LIKE THE WATER LIKE ON MY WEB SITE

```html
<!DOCTYPE html>
<html lang="en">
<head>
<meta charset="utf-8">
<title>Brixen Taplor – Business Card</title>
<link rel="stylesheet" href="https://fonts.googleapis.com/css2?family=Montserrat:wght@400;500;600;700&display=swap">
<style>
  :root {
    --stage: #d9dadc;
    --card-blue: #1172ad;
    --deep-blue: #0054aa;
    --mid-blue: #0677ba;
    --sky: #7badd7;
    --ice: #cadeef;
    --mist: #e8f1f8;
    --white: #ffffff;
  }
  * { box-sizing: border-box; margin: 0; padding: 0; }
  html, body {
    width: 1200px; height: 800px; overflow: hidden;
    background: var(--stage);
    font-family: "Montserrat", Arial, sans-serif;
  }
  .canvas { position: relative; width: 1200px; height: 800px; }
  .card {
    position: absolute; top: 250px;
    width: 520px; height: 300px;
    border-radius: 22px;
    background: var(--card-blue);
    box-shadow: 0 14px 30px rgba(0,0,0,0.22);
    overflow: hidden;
    color: var(--white);
  }
  .card--front { left: 60px; }
  .card--back { left: 620px; }

  .brand {
    position: absolute; right: 40px; top: 62px;
    display: flex; align-items: center; gap: 12px;
  }
  .brand__dot {
    width: 30px; height: 30px; border-radius: 50%;
    background: var(--white);
  }
  .brand__name {
    font-weight: 600; font-size: 22px; letter-spacing: 1.5px;
    color: var(--white);
  }
  .divider {
    position: absolute; left: 30px; right: 30px; top: 186px;
    height: 1px; background: var(--ice); opacity: 0.85;
  }
  .person { position: absolute; left: 30px; top: 140px; }
  .person__name { font-weight: 600; font-size: 17px; letter-spacing: 0.8px; }
  .person__role { font-size: 11px; margin-top: 3px; color: var(--mist); }

  .contacts { position: absolute; left: 30px; top: 198px; list-style: none; }
  .contacts li {
    display: flex; align-items: center; gap: 9px;
    font-size: 11px; line-height: 19px; color: var(--mist);
  }
  .contacts svg { width: 10px; height: 10px; flex: none; }

  .address {
    position: absolute; right: 30px; top: 198px;
    text-align: right; font-size: 11px; line-height: 17px; color: var(--mist);
  }

  .pattern-area {
    position: absolute; inset: 0;
    background: linear-gradient(120deg, #e9eef2 0%, #8fb3cc 25%, var(--mid-blue) 50%, #0c3f66 78%, #101a24 100%);
    opacity: 0.9;
  }
</style>
</head>
<body>
<main class="canvas">

  <section class="card card--front" aria-label="Business card front">
    <div class="brand">
      <span class="brand__dot"></span>
      <span class="brand__name">BRIXEN TAPLOR</span>
    </div>

    <div class="person">
      <p class="person__name">DORIAN VALE</p>
      <p class="person__role">Founder &amp; CEO</p>
    </div>

    <div class="divider"></div>

    <ul class="contacts">
      <li>
        <svg viewBox="0 0 10 10"><path d="M2 1 L4 1 L4.6 3 L3.4 3.8 Q4.5 5.8 6.2 6.6 L7 5.4 L9 6 L9 8 Q5 9 1.8 5 Q1 3 2 1Z" fill="#ffffff"/></svg>
        555-014-2788
      </li>
      <li>
        <svg viewBox="0 0 10 10"><rect x="0.5" y="2" width="9" height="6" fill="#ffffff"/><path d="M0.5 2 L5 5.5 L9.5 2" stroke="#1172ad" stroke-width="0.8" fill="none"/></svg>
        info@brixentaplorllc.com
      </li>
      <li>
        <svg viewBox="0 0 10 10"><circle cx="5" cy="5" r="4.5" fill="#ffffff"/><path d="M0.5 5 H9.5 M5 0.5 Q2.5 5 5 9.5 M5 0.5 Q7.5 5 5 9.5" stroke="#1172ad" stroke-width="0.7" fill="none"/></svg>
        brixentaplorllc.com
      </li>
    </ul>

    <address class="address">
      Brixen Taplor Group<br>
      4120 Juniper Court<br>
      Fairbanks, Alaska 99701
    </address>
  </section>

  <section class="card card--back" aria-label="Business card back">
    <div class="pattern-area" role="img" aria-label="Repeating foil-finish brand pattern in silver and dark blue over the card blue"></div>
  </section>

</main>
</body>
</html>
```